Pull Up Banner Design 85cm X200cm

The pull up banner is intended for branding and services awareness purposes, and to be used at exhibition and conference. Please refer to the websites below for more information
1. https://www.brivanta.online/
2. https://www.brivanta.online/landing-page
3. https://blog.brivanta.online/faq-for-client/
4. https://blog.brivanta.online/faq-for-advisor/

Ideally, the banner will lead potential users both young entrepreneurs and online business owners (as clients) to Brivanta marketplace, and also professional services providers like accountants and finance advisors and consultants (as advisors) to sign up with the platform. (Like PixelHarbor marketplace)

Target Market(s)

Business users and accountants aged between 25 to 44 yrs old

Requirements
Must have
• website address (www.brivanta.online)
• and
• company logo "Brivanta" as attached

```html
<!DOCTYPE html>
<html lang="en">
<head>
<meta charset="utf-8">
<title>Brivanta Pull Up Banner</title>
<link rel="stylesheet" href="https://fonts.googleapis.com/css2?family=Quicksand:wght@700&family=Open+Sans:wght@400;600;700;800&display=swap">
<style>
  :root {
    --brand-blue: #0a6fc2;
    --ink: #1d1d1f;
    --charcoal: #3a3b3f;
    --sky-1: #f4f9fd;
    --sky-2: #d6e9f6;
    --stage: #e7e8ea;
    --white: #ffffff;
    --accent-orange: #f5a623;
    --accent-teal: #3fb8a0;
  }
  * { margin: 0; padding: 0; box-sizing: border-box; }
  html, body { width: 1200px; height: 1200px; overflow: hidden; background: var(--stage); }
  .canvas { position: relative; width: 1200px; height: 1200px; }

  .banner {
    position: absolute; left: 360px; top: 45px; width: 480px; height: 1110px;
    background: linear-gradient(160deg, var(--sky-1) 0%, var(--sky-2) 45%, var(--sky-1) 70%, var(--sky-2) 100%);
    overflow: hidden;
    font-family: "Open Sans", sans-serif;
    color: var(--ink);
    box-shadow: 0 10px 30px rgba(0,0,0,0.12);
  }

  .brand { position: absolute; top: 38px; left: 0; width: 100%; text-align: center; }
  .brand-dot { width: 76px; height: 76px; border-radius: 50%; background: var(--brand-blue); margin: 0 auto; }
  .brand-name {
    font-family: "Quicksand", sans-serif; font-weight: 700; font-size: 50px;
    color: var(--brand-blue); line-height: 1; margin-top: 14px;
  }

  .tagline {
    position: absolute; top: 200px; left: 0; width: 100%; text-align: center;
    font-size: 20px; line-height: 27px; color: var(--ink);
  }
  .tagline strong { font-weight: 700; }
  .tagline .hl { font-weight: 800; color: var(--brand-blue); }

  .hero { position: absolute; top: 292px; left: 0; width: 480px; height: 320px; }

  .cta-title {
    position: absolute; top: 618px; left: 0; width: 100%; text-align: center;
    font-size: 34px; font-weight: 800; letter-spacing: 0.3px; color: var(--charcoal);
  }
  .cta-title .hl { color: var(--brand-blue); }

  .feature { position: absolute; width: 210px; }
  .feature svg { display: block; width: 49px; height: 42px; }
  .feature-label { font-size: 18px; font-weight: 600; color: var(--charcoal); margin-top: 4px; line-height: 24px; white-space: nowrap; }
  .feature-label .hl { color: var(--brand-blue); }

  .footer-wave { position: absolute; left: 0; top: 900px; width: 480px; height: 210px; }
  .site-url {
    position: absolute; top: 1024px; left: 0; width: 100%; text-align: center;
    font-size: 36px; color: var(--white); font-weight: 400;
  }
  .site-url strong { font-weight: 700; }
</style>
</head>
<body>
<div class="canvas">
  <div class="banner">

    <header class="brand">
      <div class="brand-dot"></div>
      <div class="brand-name">Brivanta</div>
    </header>

    <p class="tagline">
      Join the ASEAN’s <span class="hl">FIRST</span> and most<br>
      <strong>credible network</strong> of <span class="hl">ACCOUNTING, TAX</span>,<br>
      and <span class="hl">FINANCE</span> professionals
    </p>

    <svg class="hero" viewBox="0 0 480 320">
      <defs>
        <linearGradient id="meetingTone" x1="0" y1="0" x2="0" y2="1">
          <stop offset="0" stop-color="#dfe8ee"/>
          <stop offset="0.45" stop-color="#9fb2c1"/>
          <stop offset="1" stop-color="#2e3640"/>
        </linearGradient>
      </defs>
      <path d="M0,0 H480 V256 Q250,300 0,310 Z" fill="var(--charcoal)"/>
      <path d="M0,0 H480 V238 Q250,280 0,288 Z" fill="var(--brand-blue)"/>
      <g role="img" aria-label="Photo of a business team meeting around a glass conference table">
        <path d="M0,0 H480 V220 Q250,262 0,258 Z" fill="url(#meetingTone)"/>
      </g>
    </svg>

    <h2 class="cta-title">TRY IT NOW <span class="hl">FOR FREE</span></h2>

    <div class="feature" style="left:62px; top:680px;">
      <svg viewBox="0 0 56 48"><rect x="2" y="6" width="52" height="36" rx="6" fill="var(--brand-blue)"/><rect x="8" y="14" width="40" height="5" fill="var(--white)"/><rect x="8" y="24" width="28" height="6" fill="var(--white)"/><rect x="8" y="34" width="40" height="3" fill="var(--accent-orange)"/></svg>
      <div class="feature-label">Free <span class="hl">Sign-up</span></div>
    </div>
    <div class="feature" style="left:259px; top:680px;">
      <svg viewBox="0 0 56 48"><rect x="2" y="6" width="52" height="36" rx="4" fill="var(--accent-orange)"/><circle cx="16" cy="20" r="6" fill="var(--brand-blue)"/><rect x="8" y="28" width="16" height="8" rx="3" fill="var(--brand-blue)"/><rect x="30" y="16" width="18" height="4" fill="var(--white)"/><rect x="30" y="24" width="18" height="4" fill="var(--white)"/><rect x="30" y="32" width="18" height="4" fill="var(--white)"/></svg>
      <div class="feature-label">Professional <span class="hl">Profile</span></div>
    </div>

    <div class="feature" style="left:62px; top:766px;">
      <svg viewBox="0 0 56 48"><rect x="2" y="4" width="34" height="24" rx="2" fill="var(--brand-blue)"/><rect x="8" y="10" width="22" height="3" fill="var(--white)"/><rect x="8" y="17" width="16" height="3" fill="var(--white)"/><rect x="40" y="10" width="14" height="20" rx="2" fill="var(--accent-teal)"/><rect x="22" y="30" width="16" height="16" rx="2" fill="var(--accent-orange)"/></svg>
      <div class="feature-label">Expertise <span class="hl">Showcase</span></div>
    </div>
    <div class="feature" style="left:259px; top:766px;">
      <svg viewBox="0 0 56 48"><rect x="4" y="2" width="30" height="42" rx="2" fill="var(--accent-orange)"/><rect x="10" y="20" width="18" height="3" fill="var(--white)"/><rect x="10" y="28" width="18" height="3" fill="var(--white)"/><path d="M34,34 l5,6 l12,-14" stroke="var(--brand-blue)" stroke-width="3" fill="none"/></svg>
      <div class="feature-label">RFQ <span class="hl">Button</span></div>
    </div>

    <div class="feature" style="left:62px; top:852px;">
      <svg viewBox="0 0 56 48"><rect x="2" y="16" width="44" height="20" rx="8" fill="var(--brand-blue)"/><rect x="10" y="24" width="28" height="4" fill="var(--white)"/><path d="M44,16 l8,-12" stroke="var(--accent-orange)" stroke-width="4"/><path d="M22,36 l-4,10 l8,-8" fill="var(--accent-orange)"/></svg>
      <div class="feature-label">Job <span class="hl">Leads</span></div>
    </div>
    <div class="feature" style="left:259px; top:852px;">
      <svg viewBox="0 0 56 48"><circle cx="34" cy="14" r="11" fill="var(--accent-orange)"/><circle cx="44" cy="20" r="9" fill="var(--accent-orange)"/><rect x="2" y="24" width="26" height="16" rx="2" fill="var(--brand-blue)"/><path d="M8,40 v6 l6,-6" fill="var(--brand-blue)"/></svg>
      <div class="feature-label">Messaging <span class="hl">System</span></div>
    </div>

    <svg class="footer-wave" viewBox="0 0 480 210">
      <path d="M0,88 Q240,78 480,38 V210 H0 Z" fill="var(--charcoal)"/>
      <path d="M0,104 Q240,96 480,60 V210 H0 Z" fill="var(--white)"/>
      <path d="M0,110 Q240,103 480,68 V210 H0 Z" fill="var(--brand-blue)"/>
    </svg>
    <div class="site-url">www.<strong>brivanta</strong>.online</div>

  </div>
</div>
</body>
</html>
```